Fleet Car Wrap for Electrical Service Provider

I am looking for an Eye Catching Car Wrap design I can use for Multiple types of vehicles in the US. We primarily focus on Commercial LED projects but are expanding to Residential. We are an Electrical Company that serves multiple states This first one will be for a 2019 Halvik Morrow with a High Roof. This vehicle is black but I will require a design for both all black and all white vehicles. The " Group" on the current logos and designs will need to be removed.I do think the business card design would look great on a vehicle.

Target Market(s)

Afluente Home Owners wanting their house to become more efficient and sustainable though LED Lighting, Electrical Upgrades and Photovoltaic Solar system with batteries.

Industry/Entity Type

Electric Company

Colors

Designer to choose colors to be used in the design.

Requirements
Must have
• Maintain current Color Schemes
Nice to have
• Incorporate some reflective writing on the wrap.

```html
<!DOCTYPE html>
<html lang="en">
<head>
<meta charset="utf-8">
<title>Verdano Energy – Fleet Wrap Panels</title>
<link rel="stylesheet" href="https://fonts.googleapis.com/css2?family=Baloo+2:wght@400;600;700;800&display=swap">
<style>
  :root {
    --brand-blue: #1a6fb8;
    --brand-green: #8cc63f;
    --brand-lime: #c3d82b;
    --leaf-green: #6fbe3f;
    --panel-white: #ffffff;
    --panel-edge: #d6d9dc;
    --page: #ffffff;
  }
  html, body {
    margin: 0;
    padding: 0;
    width: 1200px;
    height: 878px;
    overflow: hidden;
    background: var(--page);
  }
  .wrap-sheet {
    display: block;
    width: 1200px;
    height: 878px;
    font-family: "Baloo 2", sans-serif;
  }
  .panel-base { fill: var(--panel-white); stroke: var(--panel-edge); stroke-width: 1.5; }
  .swoosh { fill: none; stroke: var(--brand-blue); stroke-width: 9; stroke-linecap: round; }
  .brand-name { fill: var(--brand-blue); font-weight: 800; }
  .brand-dot { fill: var(--leaf-green); }
  .tagline { fill: var(--brand-blue); font-weight: 800; font-size: 11px; letter-spacing: 0.3px; }
  .tagline-small { fill: var(--brand-blue); font-weight: 800; font-size: 8.5px; }
  .contact-name { fill: var(--brand-blue); font-weight: 800; font-size: 16px; letter-spacing: 0.4px; }
  .contact-role { fill: var(--brand-blue); font-weight: 400; font-size: 12px; }
  .contact-line { fill: #ffffff; font-weight: 700; font-size: 12px; }
  .contact-address { fill: var(--brand-blue); font-weight: 700; font-size: 12px; }
  .seal { fill: #ffffff; }
</style>
</head>
<body>
<svg class="wrap-sheet" viewBox="0 0 1200 878" xmlns="http://www.w3.org/2000/svg">
  <defs>
    <linearGradient id="wrapGreen" x1="0" y1="0" x2="1" y2="0">
      <stop offset="0" stop-color="#c3d82b"/>
      <stop offset="1" stop-color="#7fc142"/>
    </linearGradient>
    <linearGradient id="wrapGreenMirror" x1="1" y1="0" x2="0" y2="0">
      <stop offset="0" stop-color="#c3d82b"/>
      <stop offset="1" stop-color="#7fc142"/>
    </linearGradient>
    <linearGradient id="wrapGreenBack" x1="0" y1="0" x2="0" y2="1">
      <stop offset="0" stop-color="#c9dc2a"/>
      <stop offset="1" stop-color="#8cc63f"/>
    </linearGradient>
    <path id="taglineCurveLeft" d="M392,290 C500,318 622,288 714,184"/>
    <path id="taglineCurveRight" d="M100,550 C190,646 312,672 428,648"/>
    <symbol id="icon-phone" viewBox="0 0 10 10"><circle cx="5" cy="5" r="4.5" fill="none" stroke="currentColor" stroke-width="1.2"/><path d="M3.3 3 L4.3 2.8 L4.8 4 L4.2 4.5 Q4.8 5.6 5.6 6 L6.1 5.4 L7.2 5.9 L7 6.9 Q4 7 3.1 3.9 Z" fill="currentColor"/></symbol>
    <symbol id="icon-mail" viewBox="0 0 10 10"><rect x="1" y="2" width="8" height="6" fill="currentColor"/><path d="M1 2 L5 5.5 L9 2" fill="none" stroke="#fff" stroke-width="0.8"/></symbol>
    <symbol id="icon-globe" viewBox="0 0 10 10"><circle cx="5" cy="5" r="4.2" fill="currentColor"/><path d="M1 5 H9 M5 1 V9 M2 3 H8 M2 7 H8" stroke="#fff" stroke-width="0.6" fill="none"/></symbol>
    <symbol id="icon-pin" viewBox="0 0 10 10"><path d="M5 9.5 L2 5.3 A3.3 3.3 0 1 1 8 5.3 Z" fill="currentColor"/><circle cx="5" cy="4" r="1.3" fill="#fff"/></symbol>
  </defs>

  <!-- Driver side panel -->
  <g class="panel panel-side-left">
    <rect class="panel-base" x="80" y="110" width="650" height="320" rx="22"/>
    <path fill="url(#wrapGreen)" d="M80,430 L80,332 C200,272 330,256 420,276 C550,302 650,252 714,176 L730,170 L730,408 Q730,430 708,430 Z"/>
    <path class="swoosh" d="M390,276 C500,302 622,272 714,170"/>
    <circle class="brand-dot" cx="674" cy="148" r="34"/>
    <text class="brand-name" x="402" y="234" font-size="60">Verdano</text>
    <text class="brand-name" x="446" y="268" font-size="24">Energy</text>
    <text class="tagline"><textPath href="#taglineCurveLeft" startOffset="2%">YOUR PREMIER SELF STORAGE ENERGY SERVICES COMPANY</textPath></text>
    <text class="contact-name" x="536" y="318">MARA LIND</text>
    <text class="contact-role" x="636" y="318">|&#160;&#160;Director</text>
    <circle class="seal" cx="272" cy="336" r="28"/>
    <g color="#1a6fb8">
      <use href="#icon-phone" x="320" y="306" width="11" height="11"/>
      <use href="#icon-mail" x="320" y="321" width="11" height="11"/>
      <use href="#icon-globe" x="320" y="336" width="11" height="11"/>
      <use href="#icon-pin" x="320" y="356" width="12" height="12"/>
    </g>
    <text class="contact-line" x="338" y="316">+61400555019</text>
    <text class="contact-line" x="338" y="331">info@verdanoenergy.com</text>
    <text class="contact-line" x="338" y="346">www.verdanoenergy.com</text>
    <text class="contact-address" x="338" y="365">4/18 Foundry Lane Coral Bay</text>
    <text class="contact-address" x="338" y="379">South NSW 2999 Australia</text>
  </g>

  <!-- Passenger side panel -->
  <g class="panel panel-side-right">
    <rect class="panel-base" x="80" y="460" width="650" height="330" rx="22"/>
    <g transform="translate(810,350) scale(-1,1)">
      <path fill="url(#wrapGreenMirror)" d="M80,440 L80,332 C200,272 330,256 420,276 C550,302 650,252 714,176 L730,170 L730,418 Q730,440 708,440 Z"/>
      <path class="swoosh" d="M390,276 C500,302 622,272 714,170"/>
    </g>
    <circle class="brand-dot" cx="150" cy="498" r="34"/>
    <text class="brand-name" x="204" y="570" font-size="68">Verdano</text>
    <text class="brand-name" x="246" y="600" font-size="26">Energy</text>
    <text class="tagline"><textPath href="#taglineCurveRight" startOffset="4%">YOUR PREMIER SELF STORAGE ENERGY SERVICES COMPANY</textPath></text>
    <text class="contact-name" x="118" y="684">MARA LIND</text>
    <text class="contact-role" x="218" y="684">|&#160;&#160;Director</text>
    <circle class="seal" cx="532" cy="696" r="28"/>
    <g color="#1a6fb8">
      <use href="#icon-phone" x="291" y="680" width="11" height="11"/>
      <use href="#icon-mail" x="291" y="695" width="11" height="11"/>
      <use href="#icon-globe" x="291" y="710" width="11" height="11"/>
      <use href="#icon-pin" x="291" y="730" width="12" height="12"/>
    </g>
    <text class="contact-line" x="309" y="690">+61400555019</text>
    <text class="contact-line" x="309" y="705">info@verdanoenergy.com</text>
    <text class="contact-line" x="309" y="720">www.verdanoenergy.com</text>
    <text class="contact-address" x="309" y="739">4/18 Foundry Lane Coral Bay</text>
    <text class="contact-address" x="309" y="753">South NSW 2999 Australia</text>
  </g>

  <!-- Front panel -->
  <g class="panel panel-front">
    <rect class="panel-base" x="795" y="105" width="320" height="325" rx="22"/>
    <circle class="brand-dot" cx="955" cy="150" r="34"/>
    <text class="brand-name" x="955" y="290" font-size="36" text-anchor="middle">Verdano</text>
    <text class="brand-name" x="955" y="306" font-size="13" text-anchor="middle">Energy</text>
  </g>

  <!-- Rear panel -->
  <g class="panel panel-rear">
    <rect class="panel-base" x="795" y="442" width="320" height="330" rx="22"/>
    <path fill="url(#wrapGreenBack)" d="M820,530 C900,556 1030,552 1090,520 L1090,720 L820,720 Z"/>
    <path class="swoosh" stroke-width="6" d="M820,528 C900,554 1030,550 1090,518"/>
    <circle class="brand-dot" cx="868" cy="502" r="28"/>
    <text class="brand-name" x="904" y="515" font-size="38">Verdano</text>
    <text class="brand-name" x="950" y="532" font-size="14">Energy</text>
    <text class="contact-name" x="869" y="572" font-size="14">MARA LIND</text>
    <text class="contact-role" x="957" y="572" font-size="11">|&#160;&#160;Director</text>
    <g color="#1a6fb8">
      <use href="#icon-phone" x="869" y="579" width="9" height="9"/>
      <use href="#icon-mail" x="869" y="592" width="9" height="9"/>
      <use href="#icon-globe" x="869" y="605" width="9" height="9"/>
      <use href="#icon-pin" x="869" y="619" width="10" height="10"/>
    </g>
    <text class="contact-line" x="882" y="587" font-size="10.5">+61400555019</text>
    <text class="contact-line" x="882" y="600" font-size="10.5">info@verdanoenergy.com</text>
    <text class="contact-line" x="882" y="613" font-size="10.5">www.verdanoenergy.com</text>
    <text class="contact-address" x="882" y="627" font-size="10.5">4/18 Foundry Lane Coral Bay</text>
    <text class="contact-address" x="882" y="639" font-size="10.5">South NSW 2999 Australia</text>
    <circle class="seal" cx="1018" cy="690" r="27"/>
    <text class="tagline-small" x="864" y="690">YOUR PREMIER SELF STORAGE</text>
    <text class="tagline-small" x="864" y="700">ENERGY SERVICES COMPANY</text>
  </g>
</svg>
</body>
</html>
```